Eftpos Comparison Site requires banner adds

At QuoteNest.com.au we are a free service that allows our customers to get up to five quotes from our panel of suppliers for a range of BUSINESS related products and services. These products include eftpos / credit card machines, bank accounts, insurance, signage,office furniture etc. basically anything that a small business would need.
The process is done in 3 steps; 1) register your enquiry 2) we source and provide the five cheapest quotes 3) then select the supplier of your choice,the process is simple 123 and is FREE.

Please visit the soon to be revamped website to see our current horrible banner adds.
I require 8 banner adds with the below information
ADD 1) Get up to 10 quotes here FREE
Add 2) Australia's only EFTPOS comparison site
Add 3) Ringing everywhere for quotes.............it's so yesterday!
Add 4) Hate Eftpos Fee? Eftpos surcharging now available.
Add 5) Eftpos eating your profits? Let us put your Eftpos on a diet
Add 6) Pay less for "Norva logo" "Pelliworth Logo" "Eftpos Logo"
Add 7) Get "Flick to Buy" now
Add 8) We guarantee to get you a better deal than your bank!

Reason: I am extending your deadline because there are 8 banners and i dont want to rush you given that you have so many designs to work on.

Target Market(s)

small and medium business operators

Industry/Entity Type

Small Business

Requirements
Must have
• must have images and be bold

```html
<!DOCTYPE html>
<html lang="en">
<head>
<meta charset="utf-8">
<title>QuoteNest banner – Get up to 10 quotes here FREE</title>
<link rel="stylesheet" href="https://fonts.googleapis.com/css2?family=Figtree:wght@400;500;800;900&display=swap">
<style>
  :root {
    --canvas-bg: #ffffff;
    --frame: #a9a9a9;
    --ink: #4b4f57;
    --ink-dark: #3e3a36;
    --white: #ffffff;
    --green-top: #a6e03f;
    --green-bottom: #2e9b10;
    --blue-top: #74cdf0;
    --blue-bottom: #2a72c0;
    --orange-light: #fbc94e;
    --orange-mid: #f39a26;
    --orange-deep: #e65c00;
  }
  html, body {
    margin: 0;
    padding: 0;
    overflow: hidden;
    background: var(--canvas-bg);
  }
  .banner {
    display: block;
    width: 1200px;
    height: 301px;
    font-family: "Figtree", "Helvetica Neue", Arial, sans-serif;
  }
  .headline { font-size: 51px; font-weight: 400; fill: var(--ink); }
  .big-number { font-size: 152px; font-weight: 900; letter-spacing: -4px; }
  .digit-one { fill: url(#greenFade); }
  .digit-zero { fill: url(#blueFade); }
  .offer-here { font-size: 25px; font-weight: 500; fill: var(--ink-dark); }
  .offer-free { font-size: 58px; font-weight: 800; fill: var(--white); }
  .frame { fill: none; stroke: var(--frame); stroke-width: 1.5; }
</style>
</head>
<body>
<svg class="banner" viewBox="0 0 1200 301" xmlns="http://www.w3.org/2000/svg">
  <defs>
    <linearGradient id="greenFade" gradientUnits="userSpaceOnUse" x1="0" y1="95" x2="0" y2="200">
      <stop offset="0" stop-color="var(--green-top)"/>
      <stop offset="1" stop-color="var(--green-bottom)"/>
    </linearGradient>
    <linearGradient id="blueFade" gradientUnits="userSpaceOnUse" x1="0" y1="95" x2="0" y2="200">
      <stop offset="0" stop-color="var(--blue-top)"/>
      <stop offset="1" stop-color="var(--blue-bottom)"/>
    </linearGradient>
    <linearGradient id="bubbleFade" gradientUnits="userSpaceOnUse" x1="905" y1="0" x2="1200" y2="0">
      <stop offset="0" stop-color="var(--orange-light)"/>
      <stop offset="0.5" stop-color="var(--orange-mid)"/>
      <stop offset="1" stop-color="var(--orange-deep)"/>
    </linearGradient>
  </defs>

  <rect class="background" x="0" y="0" width="1200" height="301" fill="var(--canvas-bg)"/>

  <g class="headline-row">
    <text class="headline" x="288" y="162">Get up to</text>
    <text class="big-number" x="560" y="199"><tspan class="digit-one">1</tspan><tspan class="digit-zero">0</tspan></text>
    <text class="headline" x="737" y="162">quotes</text>
  </g>

  <g class="offer-bubble">
    <path d="M 906 301 C 893 258 915 208 968 190 L 964 166 L 990 180 C 1062 154 1160 156 1200 166 L 1200 301 Z" fill="url(#bubbleFade)"/>
    <text class="offer-here" x="935" y="283">here</text>
    <text class="offer-free" x="1007" y="277">FREE</text>
  </g>

  <rect class="frame" x="0.75" y="0.75" width="1198.5" height="299.5"/>
</svg>
</body>
</html>
```